New Business Card Design for Engineering and Surveying Company

We need a new design template for our business cards. We are a civil engineering, land surveying and pipeline integrity business. Please see dkhpartners.com for details. We need a bold, new business card design to complement our rebranding and marketing program. We have anew logo and attached vectro file. Please find additional details below. I am available to answer any questions.

Target Market(s)

Contractors, business owners, oil companies

Contact Information for Business Card

Needs to be customizable for different people (name, title, cell)

Font styles to use
Sans Serif
Other font styles liked:
• See eps file

Requirements
Must have
• Example Information:
Trevor Ashcombe

T:409-555-0173
M: 202-555-0148
tashcombe@dkhprtnrs.com

Address: 1875 Pinecrest Parkway, Beaumont, Texas 77703
Email: tolvanrey@dkhpartners.com
Website: www.dkhpartners.com
Nice to have
• I would like the back of the card to have the logo on a bold background with the text below:

[logo]
DORAN KESSLING & PARTNERS
CIVIL ENGINEERING | LAND SURVEYING | PIPELINE INTEGRITY

The reverse side should have the contact information for the person (example above), a smaller version of the logo and a graphic

```html
<!DOCTYPE html>
<html lang="en">
<head>
<meta charset="utf-8">
<title>Doran Kessling &amp; Partners – Business Card</title>
<link href="https://fonts.googleapis.com/css2?family=Rubik:wght@400;500;700&display=swap" rel="stylesheet">
<style>
  :root {
    --backdrop: #2e2e30;
    --card: #1c1c1f;
    --ink-white: #ffffff;
    --ink-grey: #5c5d62;
    --accent-red: #e2252b;
    --accent-blue: #23408f;
    --stripe-dark: #101012;
  }
  * { box-sizing: border-box; margin: 0; padding: 0; }
  html, body {
    width: 799px; height: 1200px; overflow: hidden;
    background: var(--backdrop);
    font-family: "Rubik", sans-serif;
  }
  .canvas { position: relative; width: 799px; height: 1200px; }
  .card {
    position: absolute; left: 60px;
    width: 680px; height: 390px;
    background: var(--card);
    border-radius: 4px;
    overflow: hidden;
    box-shadow: 0 14px 30px rgba(0,0,0,.45);
  }
  .card--front { top: 150px; }
  .card--back { top: 680px; }

  /* Front */
  .front-brand {
    position: absolute; left: 170px; top: 70px;
    color: var(--ink-grey);
  }
  .front-brand__mark {
    font-size: 160px; font-weight: 700; line-height: 1; letter-spacing: -4px;
  }
  .front-brand__name {
    font-size: 23px; font-weight: 500; letter-spacing: 1px; margin-top: 6px;
  }
  .services {
    position: absolute; left: 40px; bottom: 56px;
    color: var(--ink-white); font-size: 18px; letter-spacing: .5px;
  }
  .services .sep { color: var(--accent-red); margin: 0 8px; }

  /* Back */
  .back-brand {
    position: absolute; left: 40px; top: 30px;
    color: var(--ink-white);
    font-size: 70px; font-weight: 700; line-height: 1; letter-spacing: -2px;
  }
  .contacts {
    position: absolute; left: 40px; top: 112px;
    list-style: none; color: var(--ink-white); font-size: 15px;
  }
  .contacts li { display: flex; align-items: center; gap: 10px; height: 23px; }
  .contacts svg { width: 12px; height: 12px; fill: var(--accent-red); flex: none; }
  .address {
    position: absolute; right: 40px; top: 160px;
    color: var(--ink-white); font-size: 16px; line-height: 1.45; text-align: right;
  }
  .waves { position: absolute; left: 0; top: 0; width: 680px; height: 390px; }
  .person {
    position: absolute; right: 40px; bottom: 36px;
    color: var(--ink-white); text-align: left;
  }
  .person__name { font-size: 25px; font-weight: 700; }
  .person__title { font-size: 17px; margin-top: 2px; }
</style>
</head>
<body>
<main class="canvas">

  <section class="card card--front">
    <div class="front-brand">
      <div class="front-brand__mark">DKP</div>
      <div class="front-brand__name">DORAN KESSLING &amp; PARTNERS</div>
    </div>
    <p class="services">CIVIL ENGINEERING<span class="sep">|</span>LAND SURVEYING<span class="sep">|</span>PIPELINE INTEGRITY</p>
  </section>

  <section class="card card--back">
    <svg class="waves" viewBox="0 0 680 390" aria-hidden="true">
      <path d="M0 275 C150 250 270 335 430 312 C550 296 620 276 680 282 L680 390 L0 390 Z" fill="var(--accent-blue)"/>
      <path d="M0 252 C160 222 270 312 430 292 C550 278 620 256 680 262 L680 284 C620 278 550 298 430 314 C270 336 150 250 0 278 Z" fill="var(--stripe-dark)"/>
      <path d="M0 238 C160 208 270 298 430 278 C550 264 620 242 680 248 L680 262 C620 256 550 278 430 292 C270 312 160 222 0 252 Z" fill="var(--accent-red)"/>
    </svg>

    <div class="back-brand">DKP</div>

    <ul class="contacts">
      <li><svg viewBox="0 0 12 12"><path d="M2 1h2.5l1 3-1.5 1a7 7 0 0 0 3 3l1-1.5 3 1V10c0 .6-.4 1-1 1A10 10 0 0 1 1 2c0-.6.4-1 1-1z"/></svg>409-555-0173</li>
      <li><svg viewBox="0 0 12 12"><path d="M2 1h2.5l1 3-1.5 1a7 7 0 0 0 3 3l1-1.5 3 1V10c0 .6-.4 1-1 1A10 10 0 0 1 1 2c0-.6.4-1 1-1z"/></svg>202-555-0148</li>
      <li><svg viewBox="0 0 12 12"><path d="M0 2h12v8H0z"/><path d="M1 3l5 4 5-4" fill="none" stroke="var(--card)" stroke-width="1"/></svg>tashcombe@dkhprtnrs.com</li>
      <li><svg viewBox="0 0 12 12"><circle cx="6" cy="6" r="5.5"/><path d="M.5 6h11M6 .5v11M6 .5c-3 3-3 8 0 11M6 .5c3 3 3 8 0 11" fill="none" stroke="var(--card)" stroke-width=".8"/></svg>www.dkhpartners.com</li>
    </ul>

    <p class="address">1875 Pinecrest Parkway,<br>Beaumont, Texas 77703</p>

    <div class="person">
      <p class="person__name">Trevor Ashcombe</p>
      <p class="person__title">Chief Executive Officer</p>
    </div>
  </section>

</main>
</body>
</html>
```